Coastal Pulse Fiesta wordpress website

We need a wordpress design for a Brazilian dance festival event to happen in mid August in Sydney Australia.

The elevator pitch for this event is:

"Coastal Pulse Fiest is for the Social dancer who loves Brazilian rhythms and wants to have a space to dance, socialize and be inspired by a more intense experience than a regular class. As opposed to congress & festivals where there is a formality and focus on performances our events focus on relaxed and warm interactions between dance professionals and dance amateurs."

Most dances are originally from Rio de Janeiro-Brazil and we want to emphasize the cultural connection between both cities Rio (Brazil) & Sydney (Australia): beach culture, warm smiley people, love for music, dance and outdoors.

Feel free to contrast flag colours red/white/blue (Australia) & Green/yellow (Brazil)

We do not have a logo and the template / theme will be hosted on Wordpress 3.5.2
Updates

Project Deadline Extended
Reason: We still havent found anything we like and some professionals have asked more time to provide a 2nd design.

Hi everyone,

Just to let you know we've extended the deadline on this design project.

Good luck

Hi please

1. use the three uploaded pics of couples dancing as a primary feature in a banner across the page.
2. use the colours of brazil - greens, yellows and blues where possible if you have not used already.
3. Do the Heart in We Sway Tropic Dance as an actual heart image.

Thanks, looking forward to the revisions.

Cheers

Marcelo and Lucy

Target Market(s)

social dancers- men & women between 25 and 60 yo. The majority of participants are single.

Industry/Entity Type

Festival

Requirements
Must have
• Top menu to be editable via wordpress.
Nice to have
• The theme should be up, lively and fun, yet relaxed and informal.
Should not have
• Any images / sillouettes of samba Carnival women in Feathers.

```html
<!DOCTYPE html>
<html lang="en">
<head>
<meta charset="utf-8">
<title>Coastal Pulse Fiesta – Social Dance Festival</title>
<link rel="stylesheet" href="https://fonts.googleapis.com/css2?family=Arvo:ital,wght@0,400;1,700&family=Exo+2:ital,wght@1,800&family=Open+Sans:wght@400&family=Oswald:wght@500;700&family=Raleway:wght@400&display=swap">
<style>
  :root {
    --orange: #ef8240;
    --orange-light: #f7b07a;
    --orange-pale: #fbd2ab;
    --brown-dark: #3a1a0b;
    --nav-black: #121010;
    --nav-line: #3a3330;
    --cream: #fdf0c6;
    --red: #d2451e;
    --text-dark: #2a1a12;
    --white: #ffffff;
    --footer: #8a3a12;
  }
  * { box-sizing: border-box; margin: 0; padding: 0; }
  html, body { width: 1200px; height: 1200px; overflow: hidden; background: var(--cream); }
  .page { position: relative; width: 1200px; height: 1200px; overflow: hidden; font-family: "Open Sans", sans-serif; }

  /* Header */
  .site-header {
    position: absolute; left: 0; top: 0; width: 1200px; height: 186px;
    background: linear-gradient(180deg, var(--orange-pale) 0%, var(--orange-light) 55%, var(--orange) 100%);
  }
  .site-header .skyline {
    position: absolute; left: 0; bottom: 0; width: 1200px; height: 150px;
    background: linear-gradient(180deg, rgba(214,104,48,0) 0%, rgba(214,104,48,.55) 100%);
  }
  .brand { position: absolute; left: 112px; top: 60px; display: flex; align-items: center; gap: 12px; }
  .brand-mark { width: 22px; height: 22px; border-radius: 50%; background: var(--brown-dark); }
  .brand-name {
    font-family: "Oswald", sans-serif; font-weight: 500; font-size: 50px; line-height: 1;
    color: var(--brown-dark); text-transform: uppercase; letter-spacing: -0.5px;
  }

  /* Navigation */
  .main-nav {
    position: absolute; left: 0; top: 186px; width: 1200px; height: 72px;
    background: var(--nav-black); border-bottom: 2px solid var(--nav-line);
    display: flex; align-items: center; padding-left: 106px; gap: 30px;
  }
  .main-nav a { font-family: "Arvo", serif; font-size: 17px; color: var(--white); text-decoration: none; white-space: nowrap; }
  .main-nav a.is-current { background: var(--orange); border: 2px solid #f6a36d; border-radius: 4px; padding: 8px 18px; }

  /* Banner */
  .hero { position: absolute; left: 0; top: 258px; width: 1200px; height: 480px; overflow: hidden; }
  .hero-art {
    position: absolute; inset: 0;
    background:
      linear-gradient(120deg, rgba(240,225,200,.9) 0%, rgba(210,90,60,.55) 30%, rgba(40,30,60,.85) 55%, rgba(230,120,40,.8) 80%, rgba(60,140,70,.85) 100%),
      #7a3a2a;
  }
  .hero-title { position: absolute; left: 340px; top: 104px; width: 760px; text-align: center; color: var(--white); white-space: nowrap; }
  .hero-kicker { font-family: "Exo 2", sans-serif; font-style: italic; font-weight: 800; font-size: 56px; line-height: 60px; }
  .hero-sub { font-family: "Raleway", sans-serif; font-size: 46px; line-height: 52px; margin-top: 4px; letter-spacing: 1px; }
  .hero-date { font-family: "Oswald", sans-serif; font-weight: 700; font-size: 112px; line-height: 104px; margin-top: 2px; letter-spacing: 4px; }
  .hero-year { font-family: "Oswald", sans-serif; font-weight: 700; font-size: 130px; line-height: 130px; letter-spacing: 2px; }

  /* Content */
  .content { position: absolute; left: 0; top: 738px; width: 1200px; height: 272px; background: var(--cream); }
  .content-edge { position: absolute; left: 0; top: -14px; width: 1200px; height: 28px; }
  .intro { position: absolute; left: 104px; top: 28px; width: 690px; color: var(--text-dark); }
  .intro h1 { font-family: "Arvo", serif; font-style: italic; font-weight: 700; font-size: 40px; line-height: 1.1; }
  .intro h2 { font-family: "Arvo", serif; font-style: italic; font-weight: 700; font-size: 28px; line-height: 1.2; margin-top: 2px; }
  .intro p { font-size: 13.5px; line-height: 1.45; margin-top: 18px; }

  /* Booking badge */
  .book-badge {
    position: absolute; left: 835px; top: -12px; width: 212px; height: 212px; border-radius: 50%;
    background: radial-gradient(circle, var(--orange-light) 0%, var(--orange) 100%);
    display: flex; align-items: center; justify-content: center; text-decoration: none;
  }
  .book-badge-inner {
    width: 160px; height: 160px; border-radius: 50%; background: var(--cream);
    display: flex; flex-direction: column; align-items: center; justify-content: center; text-align: center;
    font-family: "Arvo", serif;
  }
  .book-title { color: var(--red); font-size: 28px; line-height: 1; font-weight: 700; }
  .book-text { color: var(--text-dark); font-size: 16px; line-height: 1.2; margin-top: 6px; }
  .book-link { color: var(--red); font-size: 16px; line-height: 1.2; }

  .social { position: absolute; left: 848px; top: 206px; display: flex; gap: 11px; }
  .social a { width: 48px; height: 48px; border-radius: 50%; background: var(--orange); border: 3px solid #f6a36d; display: block; }

  /* Crowd band */
  .crowd {
    position: absolute; left: 0; top: 1010px; width: 1200px; height: 150px;
    background: linear-gradient(180deg, var(--cream) 0%, var(--orange-light) 45%, var(--orange) 100%);
  }

  /* Footer */
  .site-footer {
    position: absolute; left: 0; top: 1160px; width: 1200px; height: 40px; background: var(--footer);
    display: flex; align-items: center; padding-left: 110px;
    color: var(--white); font-size: 15px; letter-spacing: .3px;
  }
  .site-footer .sep { margin: 0 14px; }
</style>
</head>
<body>
<div class="page">

  <header class="site-header">
    <div class="skyline" role="img" aria-label="City skyline silhouettes of a harbour city and a mountain coast in orange tones"></div>
    <div class="brand">
      <span class="brand-mark"></span>
      <span class="brand-name">Coastal Pulse Fiesta</span>
    </div>
  </header>

  <nav class="main-nav">
    <a href="#" class="is-current">Home</a>
    <a href="#">Event Information</a>
    <a href="#">Instructor Profiles</a>
    <a href="#">Timetable</a>
    <a href="#">Tickets</a>
    <a href="#">About Us</a>
    <a href="#">Contact Us</a>
  </nav>

  <section class="hero">
    <div class="hero-art" role="img" aria-label="Colourful swirling illustration with diagonal flag-coloured stripes and dancers"></div>
    <div class="hero-title">
      <div class="hero-kicker">Harbour Tropical</div>
      <div class="hero-sub">SOCIAL DANCE FESTIVAL</div>
      <div class="hero-date">22 AUGUST</div>
      <div class="hero-year">2013</div>
    </div>
  </section>

  <main class="content">
    <svg class="content-edge" viewBox="0 0 1200 28" preserveAspectRatio="none" aria-hidden="true">
      <path d="M0 14 Q25 0 50 14 T100 14 T150 14 T200 14 T250 14 T300 14 T350 14 T400 14 T450 14 T500 14 T550 14 T600 14 T650 14 T700 14 T750 14 T800 14 T850 14 T900 14 T950 14 T1000 14 T1050 14 T1100 14 T1150 14 T1200 14 L1200 28 L0 28 Z" fill="#fdf0c6"/>
    </svg>

    <article class="intro">
      <h1>Lorem ipsum dolor sit amet</h1>
      <h2>consectetuer adipiscing elit</h2>
      <p>Lorem ipsum dolor sit amet, consectetuer adipiscing elit, sed diam nonummy nibh euismod tincidunt ut laoreet dolore magna aliquam erat volutpat. Ut wisi enim ad minim veniam, quis nostrud exerci tation ullamcorper suscipit lobortis nisl ut aliquip ex ea commodo consequat. Duis autem vel eum iriure dolor in hendrerit in vulputate velit esse molestie consequat, vel illum dolore eu feugiat nulla facilisis at vero eros et accumsan et iusto odio dignissim qui blandit praesent luptatum zzril delenit augue duis dolore te feugait nulla facilisi.</p>
    </article>

    <a class="book-badge" href="#">
      <span class="book-badge-inner">
        <span class="book-title">Book<br>Now!</span>
        <span class="book-text">Jump straight<br>in to</span>
        <span class="book-link">book online!</span>
      </span>
    </a>

    <div class="social">
      <a href="#" aria-label="Social link one"></a>
      <a href="#" aria-label="Social link two"></a>
      <a href="#" aria-label="Social link three"></a>
    </div>
  </main>

  <div class="crowd" role="img" aria-label="Silhouettes of a dancing festival crowd in orange tones"></div>

  <footer class="site-footer">
    <span>©2013 COASTAL PULSE FIESTA</span><span class="sep">|</span><span>ALL RIGHTS RESERVED</span>
  </footer>

</div>
</body>
</html>
```